Logo für Trockenbauarbeiten aller Art, Spachtelarbeiten und Verputzarbeiten
Zielgruppe
Gegenstand des Unternehmens ist Trockenbauarbeiten aller Art, Spachtelarbeiten und Verputzarbeiten.
Unsere Zielgruppe sind Menschen ab 30 Jahren aufwärts, wir interessieren uns für den einzelnen Hausbesitzer oder Eigentumswohnungbesitzer. Wir benötigen einen hohen Wiedererkennungseffekt.
Wir benötigen Designvorlagen für eine Facebook Seite, Instagram und werden über diese beiden Plattformen auch Werbung schalten, daher benötigen wir dafür auch die verschiedenen Designvorlagen, um verschiedenen Werbekampangen zu erstellen.
Name des Unternehmens: 'WAND-PLAN KOLLHAGEN GmbH'
Aufgabenstellung
Wichtig ist bei den verschiedenen Designs, dass wir Leads bzw. Kundenaufträge sammeln können. Wir müssen herausstechen aus der Masse an Handwerkern. Wir sind die absoluten Spezialisten in unserem Gebiet. Des Weiteren werden wir aus den Materialen diverse Kampagnen erstellen die das komplette Jahr 2022 durchlaufen werden. Vorzugsweise werden wir hierfür die Plattfirm Facebook verwenden, aber auch andere Kanäle.
WICHTIG: Das Logo mit dem roten Haus ist unser original Logo!

```html
<!DOCTYPE html>
<html lang="de">
<head>
<meta charset="utf-8">
<title>WAND-PLAN KOLLHAGEN – Leistungen</title>
<link rel="stylesheet" href="https://fonts.googleapis.com/css2?family=Montserrat:wght@800&display=swap">
<style>
  :root {
    --bg: #211e1a;
    --panel: #2a2522;
    --red: #ed1c1c;
    --white: #ffffff;
    --ink: #1f1d1b;
    --card-edge: #e9e6e2;
  }
  * { margin: 0; padding: 0; box-sizing: border-box; }
  html, body { width: 1200px; height: 1200px; overflow: hidden; background: var(--bg); }
  body { font-family: "Montserrat", Arial, sans-serif; font-weight: 800; }
  .canvas { position: relative; width: 1200px; height: 1200px; }
  .artboard {
    position: absolute; left: 37px; top: 178px; width: 1126px; height: 844px;
    background: var(--panel); overflow: hidden;
  }
  .room-photo {
    position: absolute; left: 0; top: 0; width: 641px; height: 844px;
    background:
      linear-gradient(180deg, rgba(0,0,0,0) 0%, rgba(0,0,0,0) 76%, #b98a5c 77%, #a0724a 100%),
      linear-gradient(90deg, #d8d3cd 0%, #e6e2dd 45%, #cfcac4 71%, #4c4744 72%, #3f3a37 100%);
  }
  .brand {
    position: absolute; left: 64px; top: 62px;
    display: flex; align-items: center; gap: 14px;
    color: var(--white); font-size: 34px; line-height: 1.05; letter-spacing: 0.5px;
  }
  .brand-mark { width: 22px; height: 22px; background: var(--red); flex: none; }
  .service-card {
    position: absolute; height: 129px; background: var(--white);
    border: 3px solid var(--card-edge); border-radius: 16px;
    display: flex; align-items: center; gap: 28px; padding-left: 30px;
    color: var(--ink); font-size: 37px; line-height: 1.02;
    box-shadow: 0 6px 18px rgba(0,0,0,0.35);
  }
  .service-card svg { width: 62px; height: 62px; flex: none; }
  .card-drywall { left: 561px; top: 81px; width: 447px; }
  .card-filling { left: 692px; top: 254px; width: 367px; }
  .card-plaster { left: 584px; top: 423px; width: 355px; }
  .claim {
    position: absolute; left: 555px; top: 602px; width: 571px; height: 242px;
    background: var(--red); color: var(--white);
    font-size: 42px; line-height: 1.2; padding: 50px 0 0 87px;
  }
</style>
</head>
<body>
<div class="canvas">
  <div class="artboard">
    <div class="room-photo" role="img" aria-label="Helles Wohnzimmer mit Holzleiter, Decke, Pflanze und Blick ins Esszimmer"></div>
    <div class="brand"><span class="brand-mark"></span><span>WAND-PLAN<br>KOLLHAGEN</span></div>

    <div class="service-card card-drywall">
      <svg viewBox="0 0 62 62" aria-hidden="true"><path d="M12 32 L26 46 L52 16" fill="none" stroke="var(--ink)" stroke-width="7" stroke-linecap="round" stroke-linejoin="round"/></svg>
      <span>TROCKENBAU-<br>ARBEITEN</span>
    </div>
    <div class="service-card card-filling">
      <svg viewBox="0 0 62 62" aria-hidden="true"><path d="M12 32 L26 46 L52 16" fill="none" stroke="var(--ink)" stroke-width="7" stroke-linecap="round" stroke-linejoin="round"/></svg>
      <span>SPACHTEL-<br>ARBEITEN</span>
    </div>
    <div class="service-card card-plaster">
      <svg viewBox="0 0 62 62" aria-hidden="true"><path d="M12 32 L26 46 L52 16" fill="none" stroke="var(--ink)" stroke-width="7" stroke-linecap="round" stroke-linejoin="round"/></svg>
      <span>VERPUTZ-<br>ARBEITEN</span>
    </div>

    <div class="claim">IHRE EXPERTEN<br>FÜR SCHÖNES<br>WOHNEN.</div>
  </div>
</div>
</body>
</html>
```